Business Cards for new orthopaedic surgery practice

My husband and I are starting our own orthopaedic surgery practice. We are looking for a business card that is uniform, but one will have my name/title and the other will have his. You can just create one design with my name on it for now. But when I choose your design as the winning design I will ask that you add another copy with his name/title.

We are looking for classy, simple, elite all in one. We like dark blues/a little gold/yellow. Something that goes with our logo. We want our logo incorporated. Here is all the info you need:
Business name: RV Spine & Vitality Center
Location: 38915 North Bramble Ave
Maple Hollow, FL 33498
Phone: 954-218-4630
Fax: 954-571-2846
Email: info@myrvspine.example

Names: Lucinda Ferrow, M.D.
Board Certified Hand and Upper Extremity Surgeon

Emeka Dlunga, M.D.
Board Certified Hip & Knee Replacement/General Orthopaedic Surgeon

Can decide what you want to put on the back. Maybe a slogan:
Grounded in Care. Centered on You

I am just going to upload our logo. The only thing is if we select you as the winning design, the location, and phone numbers may change. We will need your help to update that once fully solidified.

Industry/Entity Type

Medical

Contact Information for Business Card

Colors
0054AA
0677BA
7BADD7
CADEEF
E8F1F8
0094D4
00A9DD
6FCCEA
C7EBF8
E9F6FB

Requirements
Must have
• class, appeal,
Should not have
• We want to air on the side of masculine if we are looking at masculine vs. feminine feel. But we still want it classy, sophisticated, and something we will love

```html
<!DOCTYPE html>
<html lang="en">
<head>
<meta charset="utf-8">
<title>RV Spine &amp; Vitality Center – Business Card</title>
<link rel="stylesheet" href="https://fonts.googleapis.com/css2?family=Montserrat:wght@400;500;700&family=Alegreya+Sans:wght@700&display=swap">
<style>
  :root {
    --navy: #22397a;
    --cyan: #1bb3dc;
    --paper: #f3f1f6;
    --ink: #1d2433;
    --white: #ffffff;
    --stage: #3a3a3a;
  }
  * { margin: 0; padding: 0; box-sizing: border-box; }
  html, body {
    width: 1200px; height: 554px; overflow: hidden;
    background: var(--stage);
    font-family: "Montserrat", sans-serif;
  }
  .card {
    position: absolute; top: 128px;
    width: 523px; height: 299px;
    border-radius: 16px; overflow: hidden;
  }
  .card--front { left: 68px; background: var(--paper); }
  .card--back { left: 607px; background: var(--navy); }

  .front-wave { position: absolute; inset: 0; }

  .doctor { position: absolute; left: 20px; top: 52px; }
  .doctor__name {
    font-weight: 700; font-size: 18.5px; color: var(--navy);
    letter-spacing: 0.2px;
  }
  .doctor__title {
    margin-top: 4px; font-size: 13px; font-weight: 400; color: var(--ink);
  }

  .brand {
    position: absolute; right: 20px; top: 42px;
    display: flex; align-items: center; gap: 10px;
  }
  .brand__mark {
    width: 34px; height: 34px; border-radius: 50%; background: var(--navy);
  }
  .brand__name {
    font-weight: 700; font-size: 14px; line-height: 1.25; color: var(--navy);
    text-transform: uppercase; letter-spacing: 0.4px;
  }

  .contacts {
    position: absolute; left: 20px; top: 196px; list-style: none;
  }
  .contacts li {
    display: flex; align-items: center; gap: 7px;
    height: 20.5px; font-size: 13.5px; color: var(--white);
  }
  .contacts svg { width: 13px; height: 13px; fill: var(--white); flex: none; }

  .address {
    position: absolute; right: 20px; top: 239px;
    text-align: right; font-style: normal;
    font-size: 13.5px; line-height: 19px; color: var(--white);
  }

  .back-brand {
    position: absolute; left: 0; right: 0; top: 62px;
    display: flex; flex-direction: column; align-items: center; gap: 18px;
  }
  .back-brand__mark {
    width: 60px; height: 60px; border-radius: 50%; background: var(--white);
  }
  .back-brand__name {
    font-weight: 700; font-size: 26px; line-height: 1.2; color: var(--white);
    text-transform: uppercase; letter-spacing: 1px; text-align: center;
  }
  .tagline {
    position: absolute; left: 0; right: 0; top: 251px;
    text-align: center;
    font-family: "Alegreya Sans", sans-serif; font-weight: 700; font-size: 15px;
    color: var(--white);
  }
  .tagline__lead { color: var(--cyan); }
</style>
</head>
<body>

<section class="card card--front">
  <svg class="front-wave" viewBox="0 0 523 299" preserveAspectRatio="none" aria-hidden="true">
    <path d="M7,172 C50,140 90,132 130,134 C230,138 330,180 420,186 C460,189 490,178 500,165 C470,186 430,192 400,190 C320,184 230,150 130,146 C90,144 50,150 7,172 Z" fill="var(--cyan)"/>
    <path d="M0,182 C40,160 80,150 118,150 C210,152 310,196 398,199 C450,200 495,180 523,151 L523,299 L0,299 Z" fill="var(--navy)"/>
  </svg>

  <div class="doctor">
    <h1 class="doctor__name">LUCINDA FERROW, M.D.</h1>
    <p class="doctor__title">Hand and Upper Extremity Surgery</p>
  </div>

  <div class="brand">
    <span class="brand__mark"></span>
    <span class="brand__name">RV Spine &amp;<br>Vitality<br>Center</span>
  </div>

  <ul class="contacts">
    <li>
      <svg viewBox="0 0 24 24"><path d="M3 8c3-4 15-4 18 0l-2 3-4-1V8H9v2l-4 1zM6 13h12l2 7H4z"/></svg>
      954-218-4630
    </li>
    <li>
      <svg viewBox="0 0 24 24"><path d="M7 3h10v5H7zM3 9h18v8h-3v-3H6v3H3zM7 15h10v6H7z"/></svg>
      954-571-2846
    </li>
    <li>
      <svg viewBox="0 0 24 24"><path d="M2 5h20v2l-10 6L2 7zM2 9l10 6 10-6v10H2z"/></svg>
      info@myrvspine.example
    </li>
    <li>
      <svg viewBox="0 0 24 24"><circle cx="12" cy="12" r="10"/></svg>
      www.myrvspine.example
    </li>
  </ul>

  <address class="address">
    38915 North Bramble Ave<br>
    Maple Hollow, FL 33498
  </address>
</section>

<section class="card card--back">
  <div class="back-brand">
    <span class="back-brand__mark"></span>
    <span class="back-brand__name">RV Spine &amp; Vitality<br>Center</span>
  </div>
  <p class="tagline"><span class="tagline__lead">Grounded in Care.</span> Centered on You</p>
</section>

</body>
</html>
```